Conference banner for Kestrel training organisation

We empower everyday heroes.
We provide training that empowers individuals to create positive change in themselves, their community, and the world.
We need a large banner design to promote the organisation at conferences and events. We are open to ideas and creativity.
It may involve creatively displaying our logo only, or it may involve our logo and a summary of our products (Kestrel training, Calm Minds Field Care).
Size: 820mm width x 1790mm height
300dpi
Target Market(s)
Educators and frontline health, community, and social workers.
Industry/Entity Type
Training
Colors
Designer to choose colors to be used in the design.

```html
<!DOCTYPE html>
<html lang="en">
<head>
<meta charset="utf-8">
<title>Kestrel Hub – Conference Banner</title>
<link rel="stylesheet" href="https://fonts.googleapis.com/css2?family=Mulish:wght@400;700;800&family=Questrial&display=swap">
<style>
  :root {
    --page-bg: #cbcbcb;
    --white: #ffffff;
    --brand-blue: #2a5ea8;
    --brand-red: #d0404f;
    --deep-red: #8a2a33;
    --navy: #152a4a;
    --ink-grey: #6b6b6b;
    --body-grey: #8a8a8a;
    --photo-dark: #2c2a3a;
    --photo-mid: #6a5a5e;
  }
  * { margin: 0; padding: 0; box-sizing: border-box; }
  html, body { width: 1200px; height: 1000px; overflow: hidden; background: var(--page-bg); }
  body { position: relative; font-family: "Questrial", "Mulish", sans-serif; }

  .banner {
    position: absolute; left: 381px; top: 22px; width: 438px; height: 956px;
    background: var(--white); overflow: hidden;
  }
  .hero-area {
    position: absolute; left: 0; top: 0; width: 438px; height: 260px;
    background: linear-gradient(#fff 60%, #e6e6e6);
  }
  .crowd-photo { position: absolute; left: 0; top: 0; }
  .quote-band {
    position: absolute; left: 0; top: 71px; width: 438px; height: 52px;
    background: rgba(20, 18, 40, 0.55);
    color: var(--white); padding: 7px 40px 0 54px;
  }
  .quote-band p { font-family: "Mulish", sans-serif; font-weight: 700; font-size: 9.6px; line-height: 12px; }
  .quote-band cite { display: block; text-align: right; font-style: italic; font-size: 9px; margin-right: -12px; }

  .brand {
    position: absolute; left: 0; top: 298px; width: 438px;
    display: flex; align-items: center; justify-content: center; gap: 12px;
  }
  .brand-dot { width: 22px; height: 22px; border-radius: 50%; background: var(--brand-blue); }
  .brand-name {
    font-family: "Mulish", sans-serif; font-weight: 800; font-size: 38px;
    letter-spacing: 2px; color: var(--brand-blue);
  }
  .taglines {
    position: absolute; left: 0; top: 364px; width: 438px; text-align: center;
    font-family: "Mulish", sans-serif; font-weight: 700; font-size: 15.5px;
    line-height: 22.7px; letter-spacing: 1.2px; color: var(--ink-grey);
  }

  .rule { position: absolute; left: 0; width: 438px; height: 5px; }
  .rule--red { top: 483px; background: linear-gradient(90deg, #7a2a35, var(--brand-red) 50%, #7a2a35); }
  .rule--blue { top: 493px; background: linear-gradient(90deg, #1e2f5a, var(--brand-blue) 50%, #1e2f5a); }

  .mission {
    position: absolute; left: 24px; top: 536px; width: 210px;
    font-size: 14px; line-height: 17.5px; color: var(--body-grey);
  }
  .team-photo { position: absolute; left: 229px; top: 576px; }
  .team-caption { position: absolute; left: 396px; top: 702px; font-size: 5px; color: #999; }

  .services {
    position: absolute; left: 0; top: 711px; width: 438px; height: 199px;
    background: linear-gradient(var(--brand-red), var(--deep-red));
    display: flex; justify-content: center; gap: 8px; padding-top: 24px;
  }
  .service { width: 110px; text-align: center; color: var(--white); }
  .service svg { display: block; margin: 0 auto; height: 44px; }
  .service h3 {
    margin-top: 22px; font-family: "Mulish", sans-serif; font-weight: 700;
    font-size: 6.5px; letter-spacing: 0.2px; text-transform: uppercase;
  }
  .service p { margin: 9px auto 0; width: 88px; font-size: 4.6px; line-height: 6.1px; opacity: 0.9; }

  .footer {
    position: absolute; left: 0; top: 916px; width: 438px; height: 40px;
    background: var(--navy); display: flex; align-items: center; justify-content: space-around;
    padding: 0 40px 0 48px; color: #cfd6e2; font-size: 6px; font-family: "Mulish", sans-serif; font-weight: 700;
  }
  .social { display: flex; align-items: center; gap: 4px; }
  .social-dot { width: 10px; height: 10px; background: #b9c2d2; border-radius: 2px; }
</style>
</head>
<body>
  <main class="banner">
    <section class="hero-area">
      <svg class="crowd-photo" width="438" height="238" role="img" aria-label="Photograph of a large cheering crowd at a community event">
        <defs>
          <linearGradient id="crowd" x1="0" y1="0" x2="0" y2="1">
            <stop offset="0" stop-color="#6a6a52"/>
            <stop offset="0.35" stop-color="var(--photo-mid)"/>
            <stop offset="1" stop-color="var(--photo-dark)"/>
          </linearGradient>
        </defs>
        <polygon points="0,0 438,0 438,180 219,238 0,180" fill="url(#crowd)"/>
      </svg>
      <div class="quote-band">
        <p>“Never doubt that a small group of thoughtful, committed citizens can change the world; indeed, it’s the only thing that ever has.”</p>
        <cite>Mara Linden</cite>
      </div>
    </section>

    <div class="brand">
      <span class="brand-dot"></span>
      <span class="brand-name">KESTREL HUB</span>
    </div>

    <div class="taglines">
      <p>Fulfil your potential.</p>
      <p>Overcome challenges.</p>
      <p>Re-write your story.</p>
      <p>Become an everyday hero.</p>
    </div>

    <div class="rule rule--red"></div>
    <div class="rule rule--blue"></div>

    <p class="mission">You have the power to create positive change in yourself, your community, and your world. Ordinary people can do extraordinary things.</p>

    <svg class="team-photo" width="176" height="133" role="img" aria-label="Group photograph of the six-person team">
      <rect width="176" height="133" fill="#f3f3f3"/>
      <rect x="8" y="20" width="160" height="113" rx="30" fill="#3a3436"/>
    </svg>
    <span class="team-caption">Our Team</span>

    <section class="services">
      <article class="service">
        <svg viewBox="0 0 44 44" aria-hidden="true">
          <circle cx="22" cy="8" r="5" fill="#fff"/>
          <path d="M15 15 h14 l6 25 h-26 z" fill="#fff"/>
        </svg>
        <h3>Everyday Kestrel Training</h3>
        <p>You’re the one you’ve been waiting for. During Kestrel training, you’ll build skills and knowledge to become an everyday helper. Learn to grow self-awareness, a growth mindset, and stand up to social pressures. Gain practical tools and resources to foster change in yourself, your community, and the world.</p>
      </article>
      <article class="service">
        <svg viewBox="0 0 44 44" aria-hidden="true">
          <circle cx="20" cy="20" r="15" fill="none" stroke="#fff" stroke-width="4"/>
          <circle cx="14" cy="20" r="2" fill="#fff"/>
          <circle cx="20" cy="20" r="2" fill="#fff"/>
          <circle cx="26" cy="20" r="2" fill="#fff"/>
          <line x1="31" y1="31" x2="40" y2="40" stroke="#fff" stroke-width="5" stroke-linecap="round"/>
        </svg>
        <h3>Mindfulness Classes</h3>
        <p>Learn and practise mindfulness for everyday use. Mindfulness helps everyday people to be more aware of themselves and others. Through practical and experiential sessions, your curious discovery will explore many mindful techniques on the journey toward finding what works for you.</p>
      </article>
      <article class="service">
        <svg viewBox="0 0 44 44" aria-hidden="true">
          <path d="M16 2 h12 v14 h14 v12 h-14 v14 h-12 v-14 h-14 v-12 h14 z" fill="#fff"/>
        </svg>
        <h3>Calm Minds Field Care</h3>
        <p>Gain knowledge and skills to provide short term support to those facing a mental health problem. Learn about depression, anxiety, psychosis, and substance use problems. Gain the ability to recognise and respond to crises, including suicidal thoughts, self-harm, and more.</p>
      </article>
    </section>

    <footer class="footer">
      <span class="social"><span class="social-dot"></span>KestrelHubCoast</span>
      <span class="social"><span class="social-dot"></span>@kestrelhubcoast</span>
      <span class="social"><span class="social-dot"></span>@kestrelhubcoast</span>
      <span class="social"><span class="social-dot"></span>KestrelHubCoast</span>
    </footer>
  </main>
</body>
</html>
```